Brightwell Pictures Business Card

Hello,

i would like to have a dynamic, creative but tasteful card, colour used, front and back. I have attached a sample card that I liked very much from another individual to give you an idea of the theme/approach, but not colour. Ideally the graphic elements of the Brightwell Logo are brought into the design.

Target Market(s)

North America

Industry/Entity Type

Film Production

Contact Information for Business Card

Mirela Vantasch
President/Founder
Brightwell Pictures Inc.
587 914 3362
mirela@brightwellpix.tv

Font styles to use
Sans Serif

Colors
6b449b
5c5c5c
fdfdfd
000000

Requirements
Must have
• Logo, name, Company name, email and cell number. no Address line to be included.
Should not have
• any unrelated GFX elements, serif fonts

```html
<!DOCTYPE html>
<html lang="en">
<head>
<meta charset="utf-8">
<title>Brightwell Pictures – Business Card</title>
<link rel="stylesheet" href="https://fonts.googleapis.com/css2?family=Roboto:wght@400;500;700;900&display=swap">
<style>
  :root {
    --brand-purple: #6b449b;
    --brand-purple-deep: #34196a;
    --brand-purple-mid: #4a2a86;
    --ink-light: #ece6ef;
    --ink-soft: #ddd4e6;
    --stage: #e9e6e2;
    --card-frost: #d9cfc6;
  }
  * { margin: 0; padding: 0; box-sizing: border-box; }
  html, body {
    width: 1200px;
    height: 970px;
    overflow: hidden;
    background: var(--stage);
    font-family: "Roboto", Arial, sans-serif;
  }
  .business-card {
    position: absolute;
    left: 176px;
    top: 240px;
    width: 848px;
    height: 490px;
    border-radius: 14px;
    overflow: hidden;
    background: linear-gradient(100deg, var(--brand-purple) 0%, var(--brand-purple-mid) 45%, var(--brand-purple-deep) 75%);
  }
  .motif-area {
    position: absolute;
    right: 0;
    top: 0;
    width: 420px;
    height: 100%;
    background: linear-gradient(160deg, var(--card-frost) 0%, var(--brand-purple-deep) 55%, var(--brand-purple-mid) 100%);
    opacity: 0.55;
  }
  .brand-name {
    position: absolute;
    left: 50px;
    top: 52px;
    font-size: 52px;
    font-weight: 700;
    letter-spacing: -1px;
    color: var(--ink-light);
  }
  .contact-block {
    position: absolute;
    left: 50px;
    top: 188px;
    color: var(--ink-soft);
  }
  .person-name {
    font-size: 33px;
    font-weight: 500;
    color: var(--ink-light);
    line-height: 40px;
  }
  .person-role,
  .company-name {
    font-size: 22px;
    font-weight: 400;
    line-height: 31px;
  }
  .divider {
    width: 50px;
    height: 3px;
    background: var(--ink-soft);
    margin: 19px 0 24px;
  }
  .phone,
  .email {
    font-size: 21px;
    line-height: 30px;
  }
</style>
</head>
<body>
  <article class="business-card">
    <div class="motif-area" role="img" aria-label="Large geometric brand motif area"></div>
    <div class="brand-name">Brightwell Pictures</div>
    <div class="contact-block">
      <div class="person-name">Mirela Vantasch</div>
      <div class="person-role">President/Founder</div>
      <div class="company-name">Brightwell Pictures Inc</div>
      <div class="divider"></div>
      <div class="phone">587 914 3362</div>
      <div class="email">mirela@brightwellpix.tv</div>
    </div>
  </article>
</body>
</html>
```